Business Card desgin, company called Stand Fast.

I am looking for the logo colors (3) to be used on the card in whatever design you think might work. the certifications are on the back (4) on the front will be my name, Dana Whitlock, owner/instructor, phone 208.555.0193, website www.sfx-drills.example, email dw@sfx-drills.example. im flexible on fonts.

Target Market(s)

firearms owners

Industry/Entity Type

firearms training

Contact Information for Business Card

certification icons on back

```html
<!DOCTYPE html>
<html lang="en">
<head>
<meta charset="utf-8">
<title>Stand Fast — Business Card</title>
<link rel="stylesheet" href="https://fonts.googleapis.com/css2?family=Montserrat:wght@800&family=Roboto:wght@400;500&family=Libre+Baskerville:wght@400&display=swap">
<style>
  :root {
    --navy: #0d2138;
    --navy-deep: #0a1a40;
    --red: #c8192a;
    --white: #ffffff;
    --grey: #4a4a4a;
    --stage: #1c1e22;
    --badge-orange: #f26a1b;
    --badge-dark: #2b2b2b;
    --badge-blue: #1d3f7a;
  }
  * { box-sizing: border-box; margin: 0; padding: 0; }
  html, body {
    width: 1200px; height: 840px; overflow: hidden;
    background: var(--stage);
  }
  .canvas { position: relative; width: 1200px; height: 840px; }

  .card {
    position: absolute;
    width: 560px; height: 320px;
    border-radius: 20px;
    overflow: hidden;
    background: var(--white);
    border-bottom: 5px solid var(--red);
    box-shadow: 0 18px 40px rgba(0,0,0,.55);
  }

  /* ---------- Back card ---------- */
  .card-back { left: 50px; top: 70px; }
  .back-band {
    position: absolute; left: 0; top: 0; width: 100%; height: 200px;
    background: linear-gradient(120deg, var(--navy) 0%, var(--navy-deep) 55%, var(--navy) 100%);
  }
  .back-brand {
    position: absolute; left: 70px; top: 62px;
    display: flex; align-items: center; gap: 22px;
  }
  .brand-ring {
    width: 66px; height: 66px; border-radius: 50%;
    border: 6px solid var(--white);
    flex: none;
  }
  .back-name {
    font-family: "Montserrat", sans-serif; font-weight: 800;
    font-size: 36px; letter-spacing: 1px; color: var(--red);
    line-height: 1;
  }
  .back-url {
    font-family: "Libre Baskerville", serif;
    font-size: 18px; color: var(--white); letter-spacing: .5px;
    margin-top: 8px;
  }
  .badges {
    position: absolute; left: 0; top: 200px; width: 100%; height: 115px;
    display: flex; justify-content: space-around; align-items: center;
    padding: 0 30px;
  }
  .badge { width: 78px; height: 84px; }

  /* ---------- Front card ---------- */
  .card-front { left: 590px; top: 450px; }
  .front-panel { position: absolute; left: 0; top: 0; width: 330px; height: 320px; }
  .front-mark {
    position: absolute; left: 38px; top: 132px;
    display: flex; align-items: center; gap: 14px;
  }
  .front-mark .brand-ring { width: 44px; height: 44px; border: 5px solid var(--red); }
  .front-mark-name {
    font-family: "Montserrat", sans-serif; font-weight: 800;
    font-size: 30px; color: var(--white); letter-spacing: .5px; line-height: 1;
  }
  .edge-bar {
    position: absolute; right: 0; top: 38px; width: 16px; height: 58px;
    background: var(--red);
  }
  .front-info {
    position: absolute; right: 36px; top: 38px; text-align: right;
  }
  .front-company {
    font-family: "Montserrat", sans-serif; font-weight: 800;
    font-size: 30px; color: var(--red); letter-spacing: 1px; line-height: 1;
  }
  .person { margin-top: 30px; }
  .person-name {
    font-family: "Roboto", sans-serif; font-weight: 500;
    font-size: 22px; color: var(--red); text-transform: uppercase; line-height: 1.1;
  }
  .person-role {
    font-family: "Roboto", sans-serif; font-size: 17px; color: var(--grey);
  }
  .contacts { list-style: none; margin-top: 26px; }
  .contacts li {
    display: flex; justify-content: flex-end; align-items: center; gap: 8px;
    font-family: "Roboto", sans-serif; font-size: 17px; color: var(--grey);
    line-height: 1.45;
  }
  .contacts svg { width: 15px; height: 15px; flex: none; }
</style>
</head>
<body>
<main class="canvas">

  <!-- Back: brand band and certifications -->
  <section class="card card-back" aria-label="Card back">
    <div class="back-band"></div>
    <div class="back-brand">
      <span class="brand-ring"></span>
      <div>
        <p class="back-name">STAND FAST</p>
        <p class="back-url">WWW.SFX-Drills.example</p>
      </div>
    </div>
    <div class="badges">
      <svg class="badge" viewBox="0 0 78 84" role="img" aria-label="Pistol instructor certification badge">
        <path d="M39 4 L72 16 L68 54 Q60 74 39 80 Q18 74 10 54 L6 16 Z" fill="var(--badge-orange)"/>
      </svg>
      <svg class="badge" viewBox="0 0 78 84" role="img" aria-label="Instructor certification badge">
        <rect x="10" y="8" width="58" height="68" rx="12" fill="var(--badge-dark)"/>
      </svg>
      <svg class="badge" viewBox="0 0 78 84" role="img" aria-label="Range safety officer certification badge">
        <rect x="10" y="8" width="58" height="68" rx="12" fill="var(--badge-dark)"/>
      </svg>
      <svg class="badge" viewBox="0 0 78 84" role="img" aria-label="Concealed carry instructor certification badge">
        <path d="M39 4 L72 14 L68 52 Q60 72 39 80 Q18 72 10 52 L6 14 Z" fill="var(--badge-blue)"/>
      </svg>
    </div>
  </section>

  <!-- Front: identity and contact -->
  <section class="card card-front" aria-label="Card front">
    <svg class="front-panel" viewBox="0 0 330 320" aria-hidden="true">
      <path d="M0 0 H170 A160 160 0 0 1 170 320 H0 Z" fill="var(--navy)"/>
    </svg>
    <div class="front-mark">
      <span class="brand-ring"></span>
      <span class="front-mark-name">STAND FAST</span>
    </div>

    <span class="edge-bar"></span>
    <div class="front-info">
      <p class="front-company">STAND FAST</p>
      <div class="person">
        <p class="person-name">Dana Whitlock</p>
        <p class="person-role">owner / instructor</p>
      </div>
      <ul class="contacts">
        <li>208.555.0193
          <svg viewBox="0 0 16 16" aria-hidden="true"><path d="M3 1 L6 1 L7 5 L5 6.5 Q6.5 9.5 9.5 11 L11 9 L15 10 L15 13 Q15 15 13 15 Q1 14 1 3 Q1 1 3 1 Z" fill="var(--red)"/></svg>
        </li>
        <li>dw@sfx-drills.example
          <svg viewBox="0 0 16 16" aria-hidden="true"><rect x="1" y="3" width="14" height="10" rx="1.5" fill="var(--red)"/><path d="M2 4 L8 9 L14 4" stroke="var(--white)" stroke-width="1.4" fill="none"/></svg>
        </li>
        <li>www.sfx-drills.example
          <svg viewBox="0 0 16 16" aria-hidden="true"><circle cx="8" cy="8" r="7" fill="var(--red)"/><path d="M1 8 H15 M8 1 Q4 8 8 15 M8 1 Q12 8 8 15" stroke="var(--white)" stroke-width="1.1" fill="none"/></svg>
        </li>
      </ul>
    </div>
  </section>

</main>
</body>
</html>
```